A book titled The Raven Left Us A Riddle. It's intended to change peoples perspective of the streets

Title: The Raven Left Us A Riddle
Subtitile: And We Keep On Turning Its Pages. (Doesn't really have to be on the cover, you decide.)
Author: Marvin Quillingsby
Book Size: 6x9 I need a book cover design for my first book. It's a very short book 60-70 pages. It is a book that points out the tricks the devil uses to get people to run the streets. It's meant to destroy some of the patterns that have been set in place in neighborhoods that are considered bad.
I didn't want to tell people what the book was about at all so that whoever came the closest to displaying what I was thinking would be the winner. Since I have given you a snippet of what it is about, I won't lead you any further. Whatever colors, whatever theme, whatever you come up with is totally up to you.

Target Market(s)

18-35 year olds

Requirements
Must have
• At this point I don't want to interfere with the creativity that could come forth. This might be a premature decision on my part. I don't want to say add this or I don't want this. I want it to be as special as I feel the title and the book is. I want it to be compelling enough, and coincide with the title enough that someone has to pick it up to read it.
Nice to have
• At this point I don't want to interfere with the creativity that could come forth. This might be a premature decision on my part. I don't want to say add this or I don't want this.
Should not have

```html
<!DOCTYPE html>
<html lang="en">
<head>
<meta charset="utf-8">
<title>The Raven Left Us A Riddle — Book Cover</title>
<link href="https://fonts.googleapis.com/css2?family=Bebas+Neue&family=Roboto:wght@400&display=swap" rel="stylesheet">
<style>
  :root {
    --backdrop: #2b2b2b;
    --cover-black: #000000;
    --title-white: #ffffff;
    --title-red: #e30613;
    --arm-light: #ecebee;
    --arm-skin: #c9a08c;
    --arm-red: #d8090f;
  }
  html, body {
    margin: 0;
    width: 1200px;
    height: 1200px;
    overflow: hidden;
    background: var(--backdrop);
  }
  .canvas {
    width: 1200px;
    height: 1200px;
    display: flex;
    align-items: center;
    justify-content: center;
  }
  .book-cover {
    width: 760px;
    height: 1120px;
    display: block;
    background: var(--cover-black);
  }
  .title-line {
    font-family: "Bebas Neue", "Oswald", sans-serif;
  }
  .title-white { fill: var(--title-white); }
  .title-red { fill: var(--title-red); }
  .subtitle {
    font-family: "Roboto", sans-serif;
    font-weight: 400;
    font-size: 26px;
    fill: var(--title-red);
  }
  .author {
    font-family: "Bebas Neue", "Oswald", sans-serif;
    font-size: 60px;
    fill: var(--title-red);
  }
</style>
</head>
<body>
<main class="canvas">
  <svg class="book-cover" viewBox="0 0 760 1120" xmlns="http://www.w3.org/2000/svg">
    <defs>
      <linearGradient id="handshake-tones" x1="0" y1="0" x2="1" y2="0">
        <stop offset="0" stop-color="var(--arm-light)"/>
        <stop offset="0.38" stop-color="var(--arm-light)"/>
        <stop offset="0.5" stop-color="var(--arm-skin)"/>
        <stop offset="0.6" stop-color="var(--arm-red)"/>
        <stop offset="1" stop-color="var(--arm-red)"/>
      </linearGradient>
      <linearGradient id="handshake-fade" x1="0" y1="0" x2="0" y2="1">
        <stop offset="0" stop-color="#000" stop-opacity="0.85"/>
        <stop offset="0.25" stop-color="#000" stop-opacity="0"/>
        <stop offset="0.8" stop-color="#000" stop-opacity="0"/>
        <stop offset="1" stop-color="#000" stop-opacity="0.9"/>
      </linearGradient>
    </defs>

    <rect class="cover-ground" width="760" height="1120" fill="var(--cover-black)"/>

    <g class="handshake-photo" role="img" aria-label="Photo of a handshake between an arm in a white pinstripe shirt and a red devil arm with black claws">
      <rect x="0" y="503" width="760" height="287" fill="url(#handshake-tones)"/>
      <rect x="0" y="503" width="760" height="287" fill="url(#handshake-fade)"/>
    </g>

    <g class="title">
      <text class="title-line title-white" x="68" y="198" font-size="200" textLength="623" lengthAdjust="spacingAndGlyphs">THE RAVEN</text>
      <text class="title-line title-red" x="89" y="363" font-size="180" textLength="584" lengthAdjust="spacingAndGlyphs">LEFT US</text>
      <text class="title-line title-white" x="90" y="552" font-size="57" textLength="34" lengthAdjust="spacingAndGlyphs">A</text>
      <text class="title-line title-white" x="153" y="552" font-size="206" textLength="516" lengthAdjust="spacingAndGlyphs">RIDDLE</text>
    </g>

    <g class="subtitle-block">
      <text class="subtitle" x="44" y="831" textLength="678" lengthAdjust="spacing">AND WE KEEP ON</text>
      <text class="subtitle" x="186" y="872" textLength="403" lengthAdjust="spacing">TURNING ITS</text>
      <text class="subtitle" x="243" y="912" textLength="283" lengthAdjust="spacing">PAGES.</text>
    </g>

    <text class="author" x="142" y="1057" textLength="478" lengthAdjust="spacingAndGlyphs">MARVIN QUILLINGSBY</text>
  </svg>
</main>
</body>
</html>
```